Corvel Lighting needs a new website (only informative)

Corvel Lighting (Pty) Ltd imports and distributes LED lighting products to South Africa. Our existing website (www.corvel-example.co.za) is designed and implemented on a shopping cart template: Trovi-Basket.

The website needs to be redesigned. It should no longer be based on a shopping cart template, but purely informative and allow some PDF downloads. It should scale well and allow quick & easy changes by the website owner: Including adding, changing and removing products. Other information pages should also be easy to manage.

No need to design a logo. A logo and user requirement specification is uploaded with more details.

Target Market(s)

Retailers, interior designers, architects, contractors, electricians, franchises etc. with a need for energy efficient LED lighting.

Industry/Entity Type

Shopping

Font styles to use
Sans Serif

Colors
0355a3
0892cd
86cae6
86cfc6

Requirements
Must have
• Existing logo to be used.
All pages informative & PDF download capability.
User friendly management
SEO capability

```html
<!DOCTYPE html>
<html lang="en">
<head>
<meta charset="utf-8">
<title>Corvel Lighting</title>
<link href="https://fonts.googleapis.com/css2?family=Open+Sans:wght@400;600;700&display=swap" rel="stylesheet">
<style>
:root{
  --navy:#0355a3;
  --blue:#0892cd;
  --sky:#86cae6;
  --mint:#86cfc6;
  --ink:#333;
  --muted:#666;
  --line:#ddd;
  --deep:#033f7a;
}
*{box-sizing:border-box;margin:0;padding:0}
html,body{width:859px;height:1200px;overflow:hidden}
body{font-family:"Open Sans",Arial,sans-serif;color:var(--ink);background:#fff;position:relative}
.header{height:57px;display:flex;align-items:center;justify-content:space-between;padding:0 40px 0 32px}
.brand{display:flex;align-items:center;gap:8px;font-weight:700;font-size:22px;color:var(--navy)}
.brand-mark{width:14px;height:14px;background:var(--blue)}
.brand small{display:block;font-size:9px;font-weight:600;letter-spacing:2px;color:var(--navy)}
.nav{display:flex;gap:26px;font-size:9px;font-weight:600;color:var(--navy)}
.hero{position:absolute;top:63px;left:0;width:859px;height:217px;background:linear-gradient(180deg,#e9edf2,#c9d2dc 70%,#b6c0cb)}
.hero-arrow{position:absolute;top:96px;width:14px;height:24px}
.tagline{position:absolute;top:286px;width:100%;text-align:center;font-size:18px;line-height:26px;color:var(--navy)}
.actions{position:absolute;top:350px;width:100%;display:flex;justify-content:center;gap:12px}
.btn{display:flex;align-items:center;height:42px;background:var(--navy);color:#fff;font-size:17px}
.btn span{padding:0 16px}
.btn i{width:30px;height:42px;background:var(--deep);display:flex;align-items:center;justify-content:center}
.info{position:absolute;top:404px;left:32px;right:32px;display:flex;gap:26px}
.info section{flex:1}
.info h2{font-size:13px;font-weight:600;color:var(--navy);margin-bottom:4px}
.info p{font-size:8.5px;line-height:12.5px;color:var(--muted);margin-bottom:10px}
.band{position:absolute;top:593px;left:0;width:859px;height:238px;background:var(--blue);display:flex}
.panel{flex:1;text-align:center;color:#fff;padding-top:16px}
.panel.mid{background:var(--navy)}
.panel h3{font-size:14px;font-weight:400;margin-bottom:10px}
.panel .ph{margin:0 auto;width:120px;height:110px;border-radius:8px}
.panel p{font-size:7.5px;line-height:11px;padding:12px 40px 0}
.bar{position:absolute;top:833px;left:0;width:859px;height:40px;background:var(--navy);color:#fff;display:flex;align-items:center;padding:0 32px;font-size:11px}
.bar .dl{display:flex;align-items:center;gap:10px;flex:1}
.news{display:flex;align-items:center;gap:10px;font-size:10px}
.news .lbl{position:absolute;top:-1px;left:454px;font-size:10px}
.news input{width:190px;height:18px;border:0;background:#fff}
.footer{position:absolute;top:884px;left:32px;right:32px;display:flex;gap:30px;border-top:1px solid var(--line);padding-top:10px}
.footer div{width:160px}
.footer h4{font-size:10px;font-weight:600;color:var(--navy);margin-bottom:6px}
.footer li{list-style:none;font-size:8.5px;line-height:14px;color:var(--muted)}
.social{display:flex;gap:6px}
.social b{width:22px;height:22px;border-radius:50%;background:var(--blue);display:block}
.copy{position:absolute;top:1158px;width:100%;text-align:center;font-size:8px;color:var(--muted);border-top:1px solid var(--line);padding-top:8px;left:0}
</style>
</head>
<body>
<header class="header">
  <div class="brand"><span class="brand-mark"></span><div>Corvel<small>LED LIGHTS</small></div></div>
  <nav class="nav"><span>COMPANY PROFILE</span><span>LIGHTING FUNDAMENTALS</span><span>PRODUCTS</span><span>CONTACT</span><span>REFERENCES</span></nav>
</header>

<div class="hero" role="img" aria-label="LED bulb and spotlight product photograph">
  <svg class="hero-arrow" style="left:8px" viewBox="0 0 14 24"><path d="M11 3 3 12l8 9" fill="none" stroke="#fff" stroke-width="3"/></svg>
  <svg class="hero-arrow" style="right:8px" viewBox="0 0 14 24"><path d="M3 3l8 9-8 9" fill="none" stroke="#fff" stroke-width="3"/></svg>
</div>

<p class="tagline">We believe in a cleaner tomorrow. Join us in conserving power. We enable you<br>through efficient &amp; affordable LED products.</p>

<div class="actions">
  <a class="btn"><span>Login</span><i><svg width="10" height="12" viewBox="0 0 10 12"><path d="M2 1l6 5-6 5" fill="none" stroke="#fff" stroke-width="2"/></svg></i></a>
  <a class="btn"><span>Register</span><i><svg width="10" height="12" viewBox="0 0 10 12"><path d="M2 1l6 5-6 5" fill="none" stroke="#fff" stroke-width="2"/></svg></i></a>
</div>

<div class="info">
  <section>
    <h2>About Us</h2>
    <p>Founded in 2009 Corvel is operated mainly by qualified electronic engineers in a manner to minimise cost in order to deliver exceptional value to our customers. We source carefully, keep offices in general warehouse space and pass every saving to our clients. Most of our company operations are automated, which allows time to be spent on product research and price negotiation with manufacturers local and abroad.</p>
  </section>
  <section>
    <h2>Why Corvel</h2>
    <p>All products are thoroughly evaluated, tested and benchmarked with competing products on the market. The above evaluation is only performed by university graduated electronic engineers.</p>
    <h2>Vision</h2>
    <p>To ensure a cleaner tomorrow through LED technology.</p>
    <h2>Mission</h2>
    <p>To research, source and promote leading edge technology at the best possible price.</p>
  </section>
</div>

<div class="band">
  <div class="panel">
    <h3>LED Products</h3>
    <div class="ph" role="img" aria-label="LED bulb product photograph" style="background:linear-gradient(#cfe3ef,#8fb8d4)"></div>
    <p>Our LED range covers bulbs, downlights, tubes and panels. Each product is tested for output, lifespan and efficiency before it reaches your shelves.</p>
  </div>
  <div class="panel mid">
    <h3>Solar Products</h3>
    <div class="ph" role="img" aria-label="Solar lantern product photograph" style="background:linear-gradient(#f3d36b,#8a7a3a)"></div>
    <p>Our solar products store daytime sunlight to power lighting at night. They suit homes, farms and sites with no grid connection at all.</p>
  </div>
  <div class="panel">
    <h3>Smart Grid Solutions</h3>
    <div class="ph" role="img" aria-label="Smart grid light fitting photograph" style="background:linear-gradient(#e4eef4,#9ab4c6)"></div>
    <p>Our smart grid solutions let you monitor and control lighting loads to cut energy use across large buildings, franchises and industrial sites.</p>
  </div>
</div>

<div class="bar">
  <div class="dl"><svg width="18" height="18" viewBox="0 0 18 18"><circle cx="9" cy="9" r="8" fill="#fff"/><path d="M9 4v8M5 8l4 4 4-4" fill="none" stroke="#0355a3" stroke-width="2"/></svg>Download Products Catalog</div>
  <div class="news"><span class="lbl">Newsletter</span><input aria-label="Email"><span>SUBSCRIBE</span><span>UNSUBSCRIBE</span></div>
</div>

<footer class="footer">
  <div><h4>Quick Links</h4><ul><li>Home</li><li>About us</li><li>Lighting Fundamentals</li><li>References</li><li>Gift Coupons</li><li>Sitemap</li><li>Contact us</li></ul></div>
  <div><h4>Products</h4><ul><li>Downlights</li><li>Bulbs</li><li>Tubes</li><li>Panels</li><li>Strips</li><li>Flood Lights</li><li>Highbays</li></ul></div>
  <div><h4>Help</h4><ul><li>Help</li><li>Shipping &amp; Returns</li><li>Privacy Notice</li><li>Conditions of Use</li><li>Newsletter Unsubscribe</li></ul></div>
  <div><h4>Follow Us</h4><div class="social"><b></b><b></b></div></div>
</footer>

<p class="copy">Copyright © 2013 Corvel Lighting. All Rights Reserved</p>
</body>
</html>
```